Contingency Program Flyer

We need a flyer to promote a new contingency program we're offering to our customers. We sell high performance car parts online. The more they buy from us, the more they get paid when they perform well at the track. There will be a good amount of wording in the flyer. We just need a nice looking digital flyer that will stay on the website with all the full details of the program and a secondary flyer with less information that we can use to post on online forums and other places to make people aware of the program without giving them the full details of the program unless they go to the site to find out the full rules. We want the flyer to use our same color scheme on the site of orange, black, white, and gray. I'd like to include some generic graphic elements relating to high performance automotive, for example, tire marks, turbochargers, etc. I can go into more detail if necessary. There will be 3 different elements to the program for how they can get paid out for winning or performing well.

This is the first time I've used Artwork Hive which is why I chose the refundable option. I'm 100% serious and in need of the project but have no experience with this site. If the site works well for us, I will start to put up committed offers and use it more regularly as we need graphic designs on an ongoing basis.

Thanks!

Industry/Entity Type

Online

```html
<!DOCTYPE html>
<html lang="en">
<head>
<meta charset="utf-8">
<title>New Contingency Program</title>
<link rel="stylesheet" href="https://fonts.googleapis.com/css2?family=Lato:wght@400;700;900&family=Stardos+Stencil:wght@700&display=swap">
<style>
  :root {
    --orange: #f47a14;
    --black: #0d0d0d;
    --white: #ffffff;
    --panel-gray: #3f4345;
    --rule-gray: #9a9a9a;
    --header-fade: #b9b9b9;
  }
  * { box-sizing: border-box; margin: 0; padding: 0; }
  html, body { width: 1200px; height: 930px; overflow: hidden; background: var(--white); }
  .flyer {
    position: relative;
    width: 1200px;
    height: 930px;
    overflow: hidden;
    font-family: "Lato", Arial, sans-serif;
    background: var(--black);
  }
  .header-band {
    position: absolute;
    left: 0; top: 0;
    width: 1200px; height: 139px;
    background: linear-gradient(to bottom, var(--white) 0%, var(--white) 62%, var(--header-fade) 100%);
  }
  .header-rule {
    position: absolute;
    left: 0; top: 70px;
    width: 1200px; height: 2px;
    background: var(--rule-gray);
  }
  .brand {
    position: absolute;
    left: 66px; top: 52px;
    padding: 0 12px;
    background: var(--white);
    font-weight: 900;
    font-size: 34px;
    line-height: 40px;
    color: var(--orange);
    letter-spacing: -0.5px;
  }
  .headline-new {
    position: absolute;
    left: 86px; top: 210px;
    font-family: "Stardos Stencil", "Times New Roman", serif;
    font-weight: 700;
    font-size: 262px;
    line-height: 230px;
    color: var(--orange);
    letter-spacing: 0;
    white-space: nowrap;
    transform: scaleX(0.93);
    transform-origin: left top;
  }
  .headline-sub {
    position: absolute;
    left: 86px; top: 396px;
    font-weight: 700;
    font-size: 53px;
    line-height: 62px;
    color: var(--white);
    letter-spacing: -0.3px;
    white-space: nowrap;
  }
  .summary-panel {
    position: absolute;
    left: 82px; top: 535px;
    width: 517px; height: 282px;
    background: var(--panel-gray);
    padding: 22px 10px 0 25px;
  }
  .summary-panel p {
    font-size: 29.5px;
    line-height: 30.5px;
    color: var(--white);
    white-space: nowrap;
  }
  .details-copy {
    position: absolute;
    left: 698px; top: 212px;
    font-size: 26.5px;
    line-height: 26.7px;
    color: var(--white);
    white-space: nowrap;
  }
  .engine-photo {
    position: absolute;
    left: 630px; top: 590px;
    width: 570px; height: 340px;
    background:
      radial-gradient(ellipse 38% 30% at 62% 38%, #d8d8d8 0%, #8b8b8b 40%, rgba(60,60,60,0) 100%),
      radial-gradient(ellipse 45% 40% at 60% 80%, #6d6d6d 0%, #3a3a3a 50%, rgba(13,13,13,0) 100%),
      radial-gradient(ellipse 10% 18% at 58% 25%, #b32a2a 0%, rgba(179,42,42,0) 100%),
      linear-gradient(to right, var(--black) 0%, #1c1c1c 30%, #2a2a2a 100%);
  }
</style>
</head>
<body>
  <main class="flyer">
    <header class="header-band">
      <div class="header-rule"></div>
      <div class="brand">apexlinemotors.com</div>
    </header>

    <div class="engine-photo" role="img" aria-label="Photo of a chrome V8 performance engine with air cleaner and red spark plug wires"></div>

    <h1 class="headline-new">NEW</h1>
    <h2 class="headline-sub">Contingency Program</h2>

    <section class="summary-panel">
      <p>Lorem ipsum dolor sit amet, consec-<br>tetur adipiscing elit, sed do eiusmod<br>tempor incididunt ut labore et<br>dolore magna aliqua. Ut enim ad<br>minim veniam, quis nostrud exer-<br>citation ullamco laboris nisi ut<br>aliquip ex ea commodo consequat.</p>
    </section>

    <p class="details-copy">Lorem ipsum dolor sit amet, consect-<br>etur adipiscing elit, sed do eiusmod<br>tempor incididunt ut labore et<br>dolore magna aliqua. Ut enim ad<br>minim veniam, quis nostrud exercita-<br>tion ullamco laboris nisi ut aliquip ex<br>ea commodo consequat. Duis aute<br>irure dolor in reprehenderit in<br>voluptate velit esse cillum dolore eu<br>fugiat nulla pariatur. Excepteur sint<br>occaecat cupidatat non proident,<br>sunt in culpa qui officia deserunt<br>mollit anim id est laborum.</p>
  </main>
</body>
</html>
```